Brellowin Redesign Website

Looking for a web design who can think out of the box.
Redesign of www.brellowin.com.au.
Design requirements:
- Use of many different Colors based on icon logo
- Use of nature and animal pictures that symbolize evolution, transition, metamorphosis, change, etc.
- Website background color for each page is based on Icon logo
- Website mood: Transition & Change, Water, Natural cycle, Waves, Natural evolution, Circle, Wheel,
- Landing page design with animated grafik based on logo icon
- Define colorful design flow that incorporates the website content (see attached file)
- Website development in Wix, access will be provided after final design

Target Market(s)

Non-for-profits in Health and Social sector, local small businesses

Industry/Entity Type

Community Development, Health, Aged-Care,

Coding

Coded - Design and coding required

Number of Pages Required

5+ page

Font styles to use
Sans Serif
Other font styles liked:
• MavenPro, Futura,

Colors
00AB8E
00BBA5
67D7C9
C6EFE9
E9F9F6
FFC000
F8CF3A
FAE287
FDF2CF
FEFAEE
F0912C
F2A743
F7CA91
FBE8D2
FDF5EE

Requirements
Must have
• Landing page with animated grafik, responsive design, out-of-box design, all pages and functions on current website, animated text and design ellements on all sides,
Nice to have
• use logo icon for landing page; it would be great if icon could be animated for the landing page, e.g. moving circles that coming out ot the head
Should not have
• look like a wix template, center aligments in block desciptions, corporate look

```html
<!DOCTYPE html>
<html lang="en">
<head>
<meta charset="utf-8">
<title>Brellowin</title>
<link href="https://fonts.googleapis.com/css2?family=Poppins:wght@500;600;700&display=swap" rel="stylesheet">
<style>
  :root {
    --ink: #000000;
    --white: #ffffff;
    --sidebar: #000000;
    --green: #74c043;
    --lime: #e2e833;
    --button: #72c243;
    --accent: #f2a743;
    --base: #eef0e6;
    --pink: #f0c6e2;
    --peach: #f6e6c6;
    --sky: #bfe3f0;
    --lilac: #e6cfe6;
    --mint: #dcefd6;
    --social: #3a3a3a;
  }
  * { margin: 0; padding: 0; box-sizing: border-box; }
  html, body { width: 1200px; height: 729px; overflow: hidden; }
  body {
    position: relative;
    font-family: "Poppins", sans-serif;
    color: var(--ink);
    background:
      radial-gradient(circle at 720px 60px, var(--pink) 0, transparent 280px),
      radial-gradient(circle at 1150px 80px, var(--mint) 0, transparent 260px),
      radial-gradient(circle at 770px 400px, var(--peach) 0, transparent 300px),
      radial-gradient(circle at 820px 690px, var(--sky) 0, transparent 260px),
      radial-gradient(circle at 1140px 600px, var(--lilac) 0, transparent 280px),
      radial-gradient(circle at 520px 700px, var(--mint) 0, transparent 220px),
      var(--base);
  }
  .hero-panel {
    position: absolute; inset: 0;
    background: linear-gradient(180deg, var(--green) 0%, var(--lime) 100%);
    clip-path: polygon(83px 0, 573px 0, 380px 729px, 83px 729px);
  }
  .sidebar {
    position: absolute; left: 0; top: 0; width: 83px; height: 729px;
    background: var(--sidebar);
  }
  .menu-toggle { position: absolute; left: 28px; top: 35px; }
  .social-links { position: absolute; left: 30px; top: 583px; list-style: none; }
  .social-links li {
    width: 22px; height: 22px; border-radius: 50%;
    background: var(--social); margin-bottom: 26px;
  }
  .brand {
    position: absolute; left: 120px; top: 27px;
    font-size: 28px; font-weight: 700; letter-spacing: 0.5px;
    color: var(--white);
  }
  .main-nav {
    position: absolute; top: 33px; left: 603px;
    display: flex; align-items: center;
  }
  .main-nav a {
    font-size: 18.5px; font-weight: 500; color: var(--ink);
    text-decoration: none; margin-right: 50px;
  }
  .nav-icons { position: absolute; top: 30px; left: 1076px; display: flex; gap: 44px; }
  .hero-mark {
    position: absolute; left: 400px; top: 190px; width: 200px; height: 200px;
    border-radius: 50%;
    background: var(--accent);
  }
  .hero-name {
    position: absolute; left: 246px; top: 414px;
    font-size: 94px; font-weight: 700; color: var(--ink); line-height: 1;
  }
  .hero-rule {
    position: absolute; left: 397px; top: 532px; width: 147px; height: 4px;
    background: var(--ink); border-radius: 2px;
  }
  .hero-quote {
    position: absolute; left: 750px; top: 337px; width: 420px;
    font-size: 26px; font-weight: 600; line-height: 39.6px;
  }
  .hero-quote cite { display: block; font-style: normal; }
  .cta {
    position: absolute; left: 749px; top: 566px; width: 297px; height: 46px;
    background: var(--button); color: var(--white);
    font-size: 20.5px; font-weight: 600;
    display: flex; align-items: center; justify-content: center;
    text-decoration: none;
  }
</style>
</head>
<body>
  <div class="hero-panel"></div>

  <aside class="sidebar">
    <svg class="menu-toggle" width="26" height="22" viewBox="0 0 26 22" aria-label="Menu">
      <rect x="0" y="0" width="20" height="3" fill="#fff"/>
      <rect x="0" y="6" width="26" height="3" fill="#fff"/>
      <rect x="0" y="12" width="16" height="3" fill="#fff"/>
      <rect x="0" y="18" width="26" height="3" fill="#fff"/>
    </svg>
    <ul class="social-links" aria-label="Social links">
      <li aria-label="Social profile one"></li>
      <li aria-label="Social profile two"></li>
      <li aria-label="Social profile three"></li>
    </ul>
  </aside>

  <div class="brand">BRELLOWIN</div>

  <nav class="main-nav">
    <a href="#">Home</a>
    <a href="#">About</a>
    <a href="#">Services</a>
    <a href="#">Contact</a>
  </nav>
  <div class="nav-icons">
    <svg width="28" height="28" viewBox="0 0 28 28" aria-label="Search">
      <circle cx="11" cy="11" r="8" fill="none" stroke="#000" stroke-width="3.5"/>
      <line x1="17" y1="17" x2="25" y2="25" stroke="#000" stroke-width="4" stroke-linecap="round"/>
    </svg>
    <svg width="26" height="28" viewBox="0 0 26 28" aria-label="Account">
      <circle cx="13" cy="8" r="7" fill="#000"/>
      <path d="M1 28 C1 18 25 18 25 28 Z" fill="#000"/>
    </svg>
  </div>

  <div class="hero-mark" aria-hidden="true"></div>
  <div class="hero-name">Brellowin</div>
  <div class="hero-rule"></div>

  <blockquote class="hero-quote">
    “Yesterday I was clever, so I wanted to change the world. Today I am wise, so I am changing myself.”
    <cite>— Samir Hollen</cite>
  </blockquote>

  <a class="cta" href="#">Book a Meeting</a>
</body>
</html>
```